A website design for a consultation firm

We are located in Istanbul, Turkey and offers our consultation services to customers interested in investing in Realestate, Education and Investment particularly this coming from Arab world and English speaking countries.

The site should carry our message of deep knowledge about the Turkish markets in the mentioned sectors of interest, sincerity and keenness.

The final deliverable of the winning design should include:
- The source files of the final designs. e.g. AI, PSD ..etc
- The redline markup for the design using a Specctr or any other similar tool.

Target Market(s)

English and Arabic speaking countries with a Turkish theme since we are a Turkish company

Industry/Entity Type

Consulting

Number of Pages Required

2 page

Font styles to use
Sans Serif

Requirements
Must have
• The site should serve the following main sections:
• - Why QVD?
• - Reports & studies
• - Sectors
• - Our team
• - Contact
• We need a design that could be converted into a WordPress theme.
• The design should be in English but should accommodate other languages including RTL.
• You can use the color theme you like as long as it does't dissolve the logo.
• The site should link into our accounts on the following networks:
• - Twitter
• - Facebook
• - LinkedIn
• The design should be responsive and nicely rendered on Desktop, Tablets and Smart phones.
Nice to have
• The site would be nice to balance between being informative and

```html
<!DOCTYPE html>
<html lang="en">
<head>
<meta charset="utf-8">
<title>QVD Consulting</title>
<link rel="stylesheet" href="https://fonts.googleapis.com/css2?family=Oswald:wght@500;600&family=Roboto:wght@400;500;700&display=swap">
<style>
:root{
  --navy:#0d2a5c;
  --navy-deep:#0a2150;
  --red:#e21b2c;
  --grey-bg:#ececec;
  --text:#333;
  --white:#fff;
}
*{box-sizing:border-box;margin:0;padding:0}
html,body{width:1200px;height:3136px;overflow:hidden}
body{position:relative;font-family:"Roboto",sans-serif;color:var(--text);background:var(--white)}
.abs{position:absolute}
.heading{font-family:"Oswald",sans-serif;font-weight:600;text-transform:uppercase;letter-spacing:.2px}

/* header */
.topbar{left:0;top:0;width:1200px;height:84px;background:var(--white)}
.logo{left:136px;top:6px;width:188px;height:140px;background:var(--white);border-radius:0 0 10px 10px;box-shadow:0 3px 8px rgba(0,0,0,.15);display:flex;align-items:center;justify-content:center;z-index:5}
.logo span{font-family:"Roboto",sans-serif;font-weight:700;font-size:23px;color:var(--red);white-space:nowrap}
.follow{left:690px;top:28px;display:flex;align-items:center;gap:8px;font-size:17px;color:#444}
.follow i{display:inline-block;width:26px;height:26px;border-radius:50%;background:#8a8a8a}
.lang{left:950px;top:30px;font-size:17px;color:#444}
.lang b{font-weight:400;color:var(--red)}
.nav{left:0;top:84px;width:1200px;height:41px;background:var(--navy);display:flex;padding-left:383px}
.nav a{color:var(--white);font-size:12px;text-decoration:none;line-height:41px;padding:0 16px;text-transform:uppercase;border-right:1px solid rgba(255,255,255,.15)}
.nav a.active{background:var(--red)}
.nav a:last-child{border-right:0}

/* hero */
.hero{left:0;top:125px;width:1200px;height:517px;
  background:
    linear-gradient(180deg,rgba(255,255,255,0) 70%,rgba(240,240,240,.95) 100%),
    radial-gradient(ellipse 190px 260px at 640px 260px,rgba(214,170,145,.55),rgba(214,170,145,0) 70%),
    radial-gradient(ellipse 200px 260px at 880px 330px,rgba(222,184,160,.5),rgba(222,184,160,0) 70%),
    radial-gradient(ellipse 260px 220px at 600px 470px,rgba(90,110,140,.45),rgba(90,110,140,0) 75%),
    radial-gradient(ellipse 300px 240px at 900px 470px,rgba(225,232,242,.9),rgba(225,232,242,0) 75%),
    radial-gradient(ellipse 420px 380px at 1120px 160px,rgba(170,176,168,.75),rgba(170,176,168,0) 70%),
    linear-gradient(90deg,#fbfbfb 0%,#f1f1f1 35%,#d9d9d6 55%,#c9ccc8 78%,#b2b7b1 100%)}
.hero-title{left:134px;top:325px;font-size:29px;line-height:39px;color:var(--navy);letter-spacing:-.3px}
.hero-title em{font-style:normal;color:var(--red)}
.hero-sub{left:134px;top:436px;width:400px;font-size:16px;line-height:21px;color:#333}
.btn{display:flex;align-items:center;justify-content:center;border-radius:24px;color:var(--white);font-size:16px;text-transform:uppercase}
.btn-red{background:var(--red)}
.btn-navy{background:var(--navy)}
.dots{display:flex;gap:6px}
.dots i{width:8px;height:8px;border-radius:50%;background:#999}
.dots i:first-child{background:var(--navy)}
.dots.light i{background:rgba(255,255,255,.5)}
.dots.light i:first-child{background:var(--white)}

/* search */
.search{left:0;top:642px;width:1200px;height:324px;background:var(--grey-bg)}
.sec-title{width:1200px;left:0;text-align:center;font-size:31px;color:var(--navy)}
.field{height:47px;background:var(--white);border:1px solid #ddd;display:flex;align-items:center;padding:0 12px 0 18px;font-size:16px;color:#888}
.field .sep{width:1px;height:47px;background:#ddd;margin-left:auto;margin-right:14px}

/* why + clients */
.why{left:0;top:966px;width:602px;height:363px;
  background:
    radial-gradient(ellipse 200px 120px at 120px 300px,rgba(240,150,155,.45),rgba(240,150,155,0) 70%),
    radial-gradient(ellipse 220px 200px at 520px 220px,rgba(160,30,40,.35),rgba(160,30,40,0) 70%),
    linear-gradient(135deg,#d9626c 0%,#c63a45 55%,#b8303a 100%)}
.clients{left:602px;top:966px;width:598px;height:363px;background:var(--navy)}
.why-list{left:134px;top:1070px;width:450px;list-style:none;color:var(--white)}
.why-list li{position:relative;padding-left:24px;margin-bottom:17px;font-size:14px;line-height:18px}
.why-list li b{font-weight:700;display:block}
.why-list li span{opacity:.85}
.why-list li::before{content:"";position:absolute;left:2px;top:4px;width:7px;height:7px;border-top:2px solid #fff;border-right:2px solid #fff;transform:rotate(45deg)}
.btn-ghost{border:1.5px solid var(--white);background:transparent}
.avatar{background:radial-gradient(circle at 50% 42%,#e2b49a 0%,#c4876a 38%,#8f4f36 70%,#4a2a1f 100%)}

/* developers */
.card{width:297px;height:328px;background:var(--white);border:1px solid #e2e2e2;box-shadow:0 1px 4px rgba(0,0,0,.12);border-radius:3px;overflow:hidden}
.card-img{position:relative;height:163px;border-bottom:3px solid var(--red);
  background:
    radial-gradient(ellipse 40px 140px at 148px 70px,rgba(120,110,95,.55),rgba(120,110,95,0) 80%),
    linear-gradient(180deg,#b7c2cd 0%,#c9d0d8 38%,#8e99a5 62%,#5f6b78 82%,#4a5563 100%)}
.card-pin{position:absolute;left:140px;bottom:-9px;width:16px;height:16px;background:var(--red);transform:rotate(45deg)}
.card h3{margin-top:18px;text-align:center;font-weight:500;font-size:18px;color:var(--navy)}
.card p{padding:6px 18px 0;font-size:14px;line-height:17px;color:#888}
.card-foot{position:absolute;left:0;bottom:0;width:100%;height:38px;border-top:1px solid #e5e5e5;display:flex;align-items:center;justify-content:space-between;padding:0 14px;font-size:15px;color:var(--navy)}

/* team */
.team{left:0;top:1891px;width:1200px;height:523px;
  background:
    linear-gradient(180deg,rgba(12,40,92,.95) 0%,rgba(12,40,92,.55) 22%,rgba(12,40,92,0) 45%),
    radial-gradient(ellipse 260px 150px at 520px 210px,rgba(120,145,180,.55),rgba(120,145,180,0) 75%),
    radial-gradient(ellipse 200px 170px at 900px 200px,rgba(110,135,172,.5),rgba(110,135,172,0) 75%),
    radial-gradient(ellipse 180px 120px at 150px 260px,rgba(100,125,165,.45),rgba(100,125,165,0) 75%),
    linear-gradient(180deg,#0f2d63 0%,#2a5189 42%,#244a80 58%,#16386d 75%,#0f2d63 100%)}
.member{width:220px;text-align:center;color:var(--white)}
.portrait{width:154px;height:154px;margin:0 auto;border-radius:50%;border:4px solid var(--white);box-shadow:0 0 0 2px rgba(13,42,92,.6)}
.member h4{margin-top:34px;font-size:18px;font-weight:700}
.member span{display:block;margin-top:10px;font-size:18px}

/* news */
.news{width:285px}
.news-img{height:147px;
  background:
    radial-gradient(ellipse 120px 60px at 80px 110px,rgba(70,90,120,.5),rgba(70,90,120,0) 75%),
    radial-gradient(ellipse 110px 60px at 210px 115px,rgba(60,80,110,.45),rgba(60,80,110,0) 75%),
    radial-gradient(ellipse 160px 70px at 140px 30px,rgba(255,255,255,.9),rgba(255,255,255,0) 75%),
    linear-gradient(180deg,#e8eef4 0%,#c3d0dc 45%,#93a4b7 75%,#7d8fa4 100%)}
.news-row{display:flex;gap:8px;margin-top:8px}
.date{flex:0 0 36px;height:50px;background:var(--navy);color:var(--white);text-align:center}
.date small{display:block;font-size:9px;padding-top:4px}
.date b{display:block;font-size:19px;font-weight:500}
.news h5{font-size:15px;font-weight:400;line-height:18px;color:var(--navy)}
.news p{margin:6px 0 0 44px;font-size:13px;line-height:16px;color:#999;text-align:justify}
.news a{display:block;margin:28px 0 0 44px;font-size:13px;color:var(--red);text-decoration:none}

/* footer */
.footer{left:0;top:2884px;width:1200px;height:205px;background:var(--navy)}
.foot-col{top:2919px;color:var(--white)}
.foot-col h6{font-size:14px;font-weight:400;margin-bottom:12px}
.foot-col p{font-size:11px;line-height:17px;color:#aab7cf}
.foot-col ul{list-style:none}
.foot-col li{font-size:11px;line-height:18px;color:#aab7cf;padding-left:12px;position:relative}
.foot-col li::before{content:"";position:absolute;left:0;top:6px;width:4px;height:4px;border-top:1.5px solid #fff;border-right:1.5px solid #fff;transform:rotate(45deg)}
.foot-col .contact li::before{display:none}
.bottom{left:0;top:3089px;width:1200px;height:47px;background:var(--navy-deep);color:var(--white);font-size:11px}
</style>
</head>
<body>

<!-- header -->
<div class="abs topbar"></div>
<div class="abs logo"><span>QVD Consulting</span></div>
<div class="abs follow">Follow us on : <i></i><i></i><i></i><i></i></div>
<div class="abs lang"><b>English</b> &nbsp;|&nbsp; Arabic</div>
<nav class="abs nav">
  <a class="active">Home</a><a>QVD Consulting</a><a>Properties</a><a>Services</a><a>Inverstor Relations</a><a>Contact</a>
</nav>

<!-- hero -->
<div class="abs hero" role="img" aria-label="Photo of a smiling businessman and businesswoman in a bright office"></div>
<h1 class="abs heading hero-title">The most experienced, professional and<br>corporate <em>real estate consultant</em></h1>
<p class="abs hero-sub">We Offer excellent services to its happy clients who are mainly from the GCC countries and Middle East</p>
<div class="abs btn btn-red" style="left:134px;top:518px;width:163px;height:46px">Get Started</div>
<div class="abs btn btn-navy" style="left:309px;top:518px;width:163px;height:46px">Learn More</div>
<div class="abs dots" style="left:141px;top:594px"><i></i><i></i><i></i><i></i></div>

<!-- search -->
<div class="abs search"></div>
<h2 class="abs heading sec-title" style="top:668px">Advanced Property Search</h2>
<div class="abs field" style="left:173px;top:742px;width:262px">Area<span class="sep"></span><svg width="14" height="9"><path d="M1 1l6 6 6-6" stroke="#333" stroke-width="2" fill="none"/></svg></div>
<div class="abs field" style="left:458px;top:742px;width:286px">Property Type<span class="sep"></span><svg width="14" height="9"><path d="M1 1l6 6 6-6" stroke="#333" stroke-width="2" fill="none"/></svg></div>
<div class="abs field" style="left:765px;top:742px;width:261px">Status<span class="sep"></span><svg width="14" height="9"><path d="M1 1l6 6 6-6" stroke="#333" stroke-width="2" fill="none"/></svg></div>
<div class="abs field" style="left:173px;top:819px;width:262px">Layout<span class="sep"></span><svg width="14" height="9"><path d="M1 1l6 6 6-6" stroke="#333" stroke-width="2" fill="none"/></svg></div>
<div class="abs field" style="left:458px;top:819px;width:286px">Delivery Date<span class="sep"></span><svg width="14" height="9"><path d="M1 1l6 6 6-6" stroke="#333" stroke-width="2" fill="none"/></svg></div>
<div class="abs field" style="left:765px;top:819px;width:261px">Price<span class="sep"></span><svg width="14" height="9"><path d="M1 1l6 6 6-6" stroke="#333" stroke-width="2" fill="none"/></svg></div>
<div class="abs btn btn-red" style="left:525px;top:890px;width:148px;height:44px;font-size:14px">Learn More</div>

<!-- why + clients -->
<div class="abs why" role="img" aria-label="Red-tinted photo of a laptop on a desk by an office window"></div>
<h2 class="abs heading" style="left:150px;top:990px;font-size:30px;color:#fff">Why QVD Consulting ?</h2>
<ul class="abs why-list">
  <li><b>Lorem ipsum dolor sit amet, consectetur adipiscing elit.</b><span>Ut vehicula sagittis ex, et iaculis mauris</span></li>
  <li><b>Lorem ipsum dolor sit amet, consectetur adipiscing elit.</b><span>Ut vehicula sagittis ex, et iaculis mauris</span></li>
  <li><b>Lorem ipsum dolor sit amet, consectetur adipiscing elit.</b><span>Ut vehicula sagittis ex, et iaculis mauris</span></li>
</ul>
<div class="abs btn btn-ghost" style="left:214px;top:1262px;width:150px;height:44px;font-size:14px">Learn More</div>

<div class="abs clients"></div>
<h2 class="abs heading" style="left:602px;width:598px;top:990px;text-align:center;font-size:30px;color:#fff">What out client says?</h2>
<div class="abs avatar" style="left:808px;top:1055px;width:86px;height:86px;border-radius:50%;border:3px solid #fff" role="img" aria-label="Client portrait"></div>
<div class="abs" style="left:602px;width:598px;top:1160px;text-align:center;color:#fff;font-size:17px;font-weight:700">Mira Holt</div>
<div class="abs" style="left:602px;width:598px;top:1191px;text-align:center;color:#fff;font-size:14px;line-height:18px"><b>Lorem ipsum dolor sit amet, consectetur adipiscing elit.</b><br>Ut vehicula sagittis ex, et iaculis mauris</div>
<div class="abs dots light" style="left:834px;top:1266px"><i></i><i></i><i></i><i></i></div>

<!-- developers -->
<h2 class="abs heading sec-title" style="top:1393px">Top developers in Instanbul</h2>
<div class="abs card" style="left:134px;top:1480px">
  <div class="card-img" role="img" aria-label="Photo of a tall residential tower above the city"><span class="card-pin"></span></div>
  <h3>Beylikduzu</h3>
  <p>Lorem ipsum dolor sit amet, consectetur adipiscing elit. Ut vehicula sagittis ex, et iaculis mauris</p>
  <div class="card-foot">$195.000<svg width="44" height="18"><g stroke="#0d2a5c" stroke-width="2" fill="none"><circle cx="3" cy="9" r="2"/><circle cx="14" cy="3" r="2"/><circle cx="14" cy="15" r="2"/><path d="M5 8l7-4M5 10l7 4"/><path d="M34 16l-6-6a3.5 3.5 0 0 1 6-4 3.5 3.5 0 0 1 6 4z"/></g></svg></div>
</div>
<div class="abs card" style="left:451px;top:1480px">
  <div class="card-img" role="img" aria-label="Photo of a tall residential tower above the city"><span class="card-pin"></span></div>
  <h3>Beylikduzu</h3>
  <p>Lorem ipsum dolor sit amet, consectetur adipiscing elit. Ut vehicula sagittis ex, et iaculis mauris</p>
  <div class="card-foot">$195.000<svg width="44" height="18"><g stroke="#0d2a5c" stroke-width="2" fill="none"><circle cx="3" cy="9" r="2"/><circle cx="14" cy="3" r="2"/><circle cx="14" cy="15" r="2"/><path d="M5 8l7-4M5 10l7 4"/><path d="M34 16l-6-6a3.5 3.5 0 0 1 6-4 3.5 3.5 0 0 1 6 4z"/></g></svg></div>
</div>
<div class="abs card" style="left:768px;top:1480px">
  <div class="card-img" role="img" aria-label="Photo of a tall residential tower above the city"><span class="card-pin"></span></div>
  <h3>Beylikduzu</h3>
  <p>Lorem ipsum dolor sit amet, consectetur adipiscing elit. Ut vehicula sagittis ex, et iaculis mauris</p>
  <div class="card-foot">$195.000<svg width="44" height="18"><g stroke="#0d2a5c" stroke-width="2" fill="none"><circle cx="3" cy="9" r="2"/><circle cx="14" cy="3" r="2"/><circle cx="14" cy="15" r="2"/><path d="M5 8l7-4M5 10l7 4"/><path d="M34 16l-6-6a3.5 3.5 0 0 1 6-4 3.5 3.5 0 0 1 6 4z"/></g></svg></div>
</div>

<!-- team -->
<div class="abs team" role="img" aria-label="Blue-tinted photo of a city skyline by the water"></div>
<h2 class="abs heading sec-title" style="top:1928px;color:#fff">Meet our team</h2>
<div class="abs member" style="left:118px;top:2080px"><div class="portrait avatar" role="img" aria-label="Team member portrait"></div><h4>Mira Holt</h4><span>Managing Director</span></div>
<div class="abs member" style="left:367px;top:2080px"><div class="portrait avatar" role="img" aria-label="Team member portrait"></div><h4>Dean Carver</h4><span>Managing Partner</span></div>
<div class="abs member" style="left:615px;top:2080px"><div class="portrait avatar" role="img" aria-label="Team member portrait"></div><h4>Nora Vell</h4><span>Research Director</span></div>
<div class="abs member" style="left:862px;top:2080px"><div class="portrait avatar" role="img" aria-label="Team member portrait"></div><h4>Business Consultant</h4><span>Business Consultant</span></div>
<div class="abs dots light" style="left:570px;top:2358px"><i></i><i></i><i></i><i></i></div>

<!-- news -->
<h2 class="abs heading sec-title" style="top:2444px">News and events</h2>
<div class="abs news" style="left:140px;top:2533px">
  <div class="news-img" role="img" aria-label="Photo of a busy open-plan office"></div>
  <div class="news-row"><div class="date"><small>AUG</small><b>21</b></div><h5>Lorem ipsum dolor sit amet, Lorem ipsum dolor met,</h5></div>
  <p>Lorem ipsum dolor sit amet, consectetur adipiscing elit. Ut vehicula sagittis ex, et iaculis mauris</p>
  <a>Learn More</a>
</div>
<div class="abs news" style="left:456px;top:2533px">
  <div class="news-img" role="img" aria-label="Photo of a busy open-plan office"></div>
  <div class="news-row"><div class="date"><small>AUG</small><b>21</b></div><h5>Lorem ipsum dolor sit amet, Lorem ipsum dolor met,</h5></div>
  <p>Lorem ipsum dolor sit amet, consectetur adipiscing elit. Ut vehicula sagittis ex, et iaculis mauris</p>
  <a>Learn More</a>
</div>
<div class="abs news" style="left:771px;top:2533px">
  <div class="news-img" role="img" aria-label="Photo of a busy open-plan office"></div>
  <div class="news-row"><div class="date"><small>AUG</small><b>21</b></div><h5>Lorem ipsum dolor sit amet, Lorem ipsum dolor met,</h5></div>
  <p>Lorem ipsum dolor sit amet, consectetur adipiscing elit. Ut vehicula sagittis ex, et iaculis mauris</p>
  <a>Learn More</a>
</div>

<!-- footer -->
<div class="abs footer"></div>
<div class="abs foot-col" style="left:140px;width:230px">
  <h6>A Brief About Company</h6>
  <p>Vivamus scelerisque et velit quis auctor. Pellentesque luctus, mauris vel ultricies pulvinar, est odio viverra ex, eu lacinia nibh purus laoreet massa. Morbi a pharetra nibh. Integer varius</p>
</div>
<div class="abs foot-col" style="left:439px">
  <h6>Sitemap</h6>
  <ul><li>Home</li><li>About QVD Consulting</li><li>History</li><li>Management</li><li>Investor Relations</li></ul>
</div>
<div class="abs foot-col" style="left:604px">
  <h6>Quick Links</h6>
  <ul><li>Imprint</li><li>Terms &amp; Conditions</li><li>Data Protection</li><li>Contact Us</li></ul>
</div>
<div class="abs foot-col" style="left:757px">
  <h6>Quick Links</h6>
  <ul><li>Imprint</li><li>Terms &amp; Conditions</li><li>Data Protection</li><li>Contact Us</li></ul>
</div>
<div class="abs foot-col" style="left:920px;width:160px">
  <h6>Contact Us</h6>
  <ul class="contact">
    <li><svg class="abs" style="left:0;top:4px" width="9" height="9"><path d="M1 1h3l1 2-1.5 1a5 5 0 0 0 2.5 2.5L7 5l2 1v3C4 9 0 5 1 1z" fill="#fff"/></svg>1234.555.0190</li>
    <li><svg class="abs" style="left:0;top:5px" width="9" height="7"><rect x="0.5" y="0.5" width="8" height="6" fill="#fff"/><path d="M1 1l3.5 3L8 1" stroke="#0d2a5c" fill="none"/></svg>info@qvdconsult.com</li>
    <li><svg class="abs" style="left:0;top:3px" width="8" height="11"><path d="M4 11C1 7 0 5.5 0 4a4 4 0 0 1 8 0c0 1.5-1 3-4 7z" fill="#fff"/></svg>mauris vel ultricies<br>pulvinar, est odio vix</li>
  </ul>
</div>
<div class="abs bottom">
  <span class="abs" style="left:140px;top:17px">Copyright 2016, QVD Consulting, All rights Reserved</span>
  <span class="abs" style="left:940px;top:17px">Privacy Policy &nbsp;&nbsp;|&nbsp;&nbsp; Help</span>
</div>

</body>
</html>
```